we need a business card in yellow, green and black with rounded edges. We are in the Construction and Engineering business. I need the below info included:

Neil Barton
Bluestone Engineering & Construction, Inc.
4168 Harbor Crest Road,
Santa Ana, Ca 92814
714-555-0147 Office
714-555-0192 Cell
714-555-0163 Fax
nb@bluestonexq.example

thanks for your help!

```html
<!DOCTYPE html>
<html lang="en">
<head>
<meta charset="utf-8">
<title>Bluestone Engineering &amp; Construction – Business Card</title>
<link rel="stylesheet" href="https://fonts.googleapis.com/css2?family=Open+Sans:wght@400;600;800&display=swap">
<style>
  :root {
    --page-bg: #ffffff;
    --yellow-top: #e2c327;
    --yellow-bottom: #f8ee36;
    --green: #0b8a3e;
    --green-dark: #06692d;
    --green-text: #129447;
    --black: #0b0d0c;
    --black-soft: #1b1f1d;
    --contact-yellow: #f3e232;
    --ink: #1a1a1a;
  }
  * { margin: 0; padding: 0; box-sizing: border-box; }
  html, body {
    width: 1200px; height: 900px; overflow: hidden;
    background: var(--page-bg);
    font-family: "Open Sans", sans-serif;
  }
  .card {
    position: absolute;
    left: 75px; top: 150px;
    width: 1050px; height: 600px;
    border-radius: 42px;
    overflow: hidden;
    background: radial-gradient(ellipse at 70% 70%, var(--black-soft) 0%, var(--black) 70%);
    box-shadow: 0 24px 50px rgba(0,0,0,0.18);
  }
  .card__top {
    position: absolute; left: 0; top: 0;
    width: 100%; height: 250px;
    background: linear-gradient(180deg, var(--yellow-top) 0%, var(--yellow-bottom) 100%);
  }
  .card__band {
    position: absolute; left: 0; top: 250px;
    width: 100%; height: 22px;
    background: linear-gradient(180deg, var(--green) 0%, var(--green-dark) 100%);
  }
  .brand {
    position: absolute; left: 70px; top: 46px;
    display: flex; align-items: center; gap: 28px;
  }
  .brand__mark {
    width: 170px; height: 170px;
    border-radius: 24px;
    background: var(--green);
  }
  .brand__name {
    font-weight: 800;
    font-size: 64px;
    line-height: 1;
    color: var(--green);
    letter-spacing: 0.5px;
    padding-bottom: 12px;
    border-bottom: 3px solid var(--ink);
  }
  .brand__tagline {
    margin-top: 10px;
    font-size: 26px;
    color: var(--ink);
  }
  .contact {
    position: absolute; left: 68px; top: 290px;
  }
  .contact__name {
    font-size: 34px;
    line-height: 46px;
    font-weight: 600;
    color: var(--green-text);
    margin-bottom: 10px;
  }
  .contact__list { list-style: none; }
  .contact__item {
    display: flex; align-items: flex-start; gap: 14px;
    font-size: 25px; line-height: 33px;
    color: var(--contact-yellow);
  }
  .contact__icon {
    flex: 0 0 28px; width: 28px; height: 28px; margin-top: 3px;
    fill: var(--green);
  }
</style>
</head>
<body>
  <article class="card">
    <div class="card__top"></div>
    <div class="card__band"></div>

    <header class="brand">
      <div class="brand__mark"></div>
      <div class="brand__text">
        <div class="brand__name">Bluestone</div>
        <div class="brand__tagline">Engineering &amp; Construction, Inc.</div>
      </div>
    </header>

    <section class="contact">
      <h1 class="contact__name">Neil Barton</h1>
      <ul class="contact__list">
        <li class="contact__item">
          <svg class="contact__icon" viewBox="0 0 30 30" aria-hidden="true"><path d="M15 3 L2 15 H6 V27 H12 V19 H18 V27 H24 V15 H28 Z"/></svg>
          <span>4168 Harbor Crest Road,<br>Santa Ana, Ca 92814</span>
        </li>
        <li class="contact__item">
          <svg class="contact__icon" viewBox="0 0 30 30" aria-hidden="true"><path d="M7 3 L12 3 L14 10 L10.5 12.5 C12 16 14 18 17.5 19.5 L20 16 L27 18 L27 23 C27 25 25 27 23 27 C12 26 4 18 3 7 C3 5 5 3 7 3 Z"/></svg>
          <span>714-555-0147</span>
        </li>
        <li class="contact__item">
          <svg class="contact__icon" viewBox="0 0 30 30" aria-hidden="true"><path d="M9 2 H21 A2 2 0 0 1 23 4 V26 A2 2 0 0 1 21 28 H9 A2 2 0 0 1 7 26 V4 A2 2 0 0 1 9 2 Z M10 6 V17 H20 V6 Z M11 19 H14 V21 H11 Z M16 19 H19 V21 H16 Z M11 23 H14 V25 H11 Z M16 23 H19 V25 H16 Z" fill-rule="evenodd"/></svg>
          <span>714-555-0192</span>
        </li>
        <li class="contact__item">
          <svg class="contact__icon" viewBox="0 0 30 30" aria-hidden="true"><path d="M8 3 H22 V10 H8 Z M3 11 H27 V22 H23 V18 H7 V22 H3 Z M8 19 H22 V28 H8 Z"/></svg>
          <span>714-555-0163</span>
        </li>
        <li class="contact__item">
          <svg class="contact__icon" viewBox="0 0 30 30" aria-hidden="true"><path d="M3 7 H27 V24 H3 Z"/><path d="M4.5 8.5 L15 16.5 L25.5 8.5" stroke="#0b0d0c" stroke-width="2" fill="none"/></svg>
          <span>nb@bluestonexq.example</span>
        </li>
      </ul>
    </section>
  </article>
</body>
</html>
```